family chiropractic health care team needs a modern business card design

Healthcare office with Chiropractors, Physiotherapists, Massage therapists and possibly other practitioners in the future. This is a friendly family office with patients of all ages (and lots of kids) that just moved into a new larger modern office.
Look at the website for photos of the office.
Design for the front and back of a business card required.
Text for the front:
Office logo and name of the office:
Bright Path Wellness Centre
Name of current Practitioner:
Dr. Marten Quovel B.Sc., D.C. Chiropractor
(But please include options to swap out name and title for other practitioners )

address:
218 Farrow Gate
Etobicoke ON.
K2J 6P4
Phone: 416-872-0196 (PATH)
Web site and email:
www.brightpathwellnesscentre.example
brightpathchiro@mailbox.example

2 versions of the back of the card:
1. text below
2. appointment schedule card

Text on back of card:
Chiropractic Card text on back of the card:
There is more to chiropractic than the relief of headaches and back pain! Our primary focus is the integrity of your nerve system, which controls and regulates every cell and tissue of your body. The moving bones of the spinal column can impair this vital communication link between your brain and body. We help improve the function and structure of your spine, reducing nerve system compromise. The result?
Even non-spinal related health problems can show improvement
without drugs
without surgery
regardless of age
for over a century
naturally

Appointment Card info For Back:
Please integrate design elements from the front of the card into an appointment card format.
M Tu W Th F Sat (and a line for writing on beside each one)

```html
<!DOCTYPE html>
<html lang="en">
<head>
<meta charset="utf-8">
<title>Bright Path Wellness Centre – Folded Card</title>
<link href="https://fonts.googleapis.com/css2?family=Poppins:wght@400;500;600;700&display=swap" rel="stylesheet">
<style>
  :root {
    --bg: #b9bcbe;
    --paper: #ffffff;
    --paper-grey: #e6e7e8;
    --green-dark: #4a8f22;
    --green: #6cb33f;
    --green-light: #a3d36a;
    --ink: #5b5d60;
    --ink-soft: #8a8c8f;
  }
  * { margin: 0; padding: 0; box-sizing: border-box; }
  html, body { width: 670px; height: 1200px; overflow: hidden; }
  body {
    background: var(--bg);
    font-family: "Poppins", sans-serif;
    color: var(--ink);
    display: flex;
    flex-direction: column;
    justify-content: center;
    align-items: center;
    gap: 70px;
  }
  .spread {
    width: 620px;
    height: 300px;
    display: flex;
    box-shadow: 0 6px 18px rgba(0,0,0,.18);
  }
  .panel {
    position: relative;
    width: 310px;
    height: 300px;
    overflow: hidden;
    background: var(--paper);
  }
  .panel--grey { background: var(--paper-grey); }
  .panel + .panel { border-left: 1px solid #d2d4d6; }
  .swoosh { position: absolute; inset: 0; width: 100%; height: 100%; }
  .content { position: relative; z-index: 1; height: 100%; }

  .brand {
    display: flex;
    align-items: center;
    gap: 8px;
    color: var(--green);
    font-weight: 600;
    line-height: 1.15;
    white-space: nowrap;
  }
  .brand__dot {
    flex: none;
    border-radius: 50%;
    background: var(--green);
  }

  /* Front */
  .front .content { padding: 30px 16px 0 70px; }
  .front .brand { font-size: 15px; margin: 0 0 18px -46px; }
  .front .brand__dot { width: 14px; height: 14px; }
  .practitioner__name { font-size: 12px; font-weight: 600; color: var(--ink); line-height: 1.3; }
  .practitioner__title { font-size: 10.5px; color: var(--ink-soft); margin-bottom: 10px; }
  .contact { font-style: normal; font-size: 9px; line-height: 1.55; color: var(--ink-soft); }
  .contact .gap { margin-top: 7px; }

  /* Appointment */
  .appointment .content { padding: 24px 0 0 24px; }
  .appointment__title { font-size: 17px; font-weight: 700; color: var(--green); margin-bottom: 12px; }
  .slots { list-style: none; width: 190px; }
  .slot {
    display: flex;
    align-items: center;
    height: 25px;
    border: 1px solid #9a9c9f;
    border-radius: 6px;
    padding-left: 9px;
    margin-bottom: 6px;
    font-size: 9px;
    font-weight: 500;
    color: var(--ink);
  }
  .appointment .brand { font-size: 12px; margin-top: 14px; }
  .appointment .brand__dot { width: 10px; height: 10px; }

  /* Inside logo */
  .inside-logo .content { display: flex; align-items: center; justify-content: center; padding-top: 40px; }
  .inside-logo .brand { font-size: 20px; white-space: normal; width: 220px; }
  .inside-logo .brand__dot { width: 18px; height: 18px; }

  /* Inside text */
  .about .content { padding: 40px 22px 0 22px; text-align: center; }
  .about__lead { font-size: 9px; font-weight: 600; color: var(--ink); line-height: 1.5; margin-bottom: 7px; }
  .about__body { font-size: 7.5px; color: var(--ink-soft); line-height: 1.5; margin-bottom: 9px; }
  .benefits {
    display: inline-block;
    background: var(--green-light);
    color: #fff;
    font-size: 7.4px;
    font-weight: 500;
    border-radius: 4px;
    padding: 5px 10px;
  }
</style>
</head>
<body>

<section class="spread spread--outside">
  <article class="panel front">
    <svg class="swoosh" viewBox="0 0 310 300" preserveAspectRatio="none" aria-hidden="true">
      <path d="M0 205 C 30 255 110 288 230 300 L 160 300 C 80 285 25 260 0 238 Z" fill="var(--green-light)"/>
      <path d="M0 222 C 35 262 100 290 190 300 L 170 300 C 90 288 30 262 0 232 Z" fill="var(--paper)"/>
      <path d="M0 250 C 30 275 80 292 140 300 L 0 300 Z" fill="var(--green)"/>
    </svg>
    <div class="content">
      <div class="brand"><span class="brand__dot"></span>Bright Path Wellness Centre</div>
      <p class="practitioner__name">Dr. Marten Quovel B.Sc., D.C.</p>
      <p class="practitioner__title">Chiropractor</p>
      <address class="contact">
        218 Farrow Gate<br>
        Etobicoke ON.<br>
        K2J 6P4<br>
        Phone: 416-872-0196 (PATH)
        <div class="gap">www.brightpathwellnesscentre.example<br>brightpathchiro@mailbox.example</div>
      </address>
    </div>
  </article>

  <article class="panel panel--grey appointment">
    <svg class="swoosh" viewBox="0 0 310 300" preserveAspectRatio="none" aria-hidden="true">
      <path d="M250 0 C 290 60 308 150 310 220 L 310 0 Z" fill="var(--green-dark)"/>
      <path d="M228 0 C 282 60 302 150 306 250 C 292 150 268 60 212 0 Z" fill="var(--green)"/>
    </svg>
    <div class="content">
      <h2 class="appointment__title">Appointment Card</h2>
      <ul class="slots">
        <li class="slot">M :</li>
        <li class="slot">TU :</li>
        <li class="slot">W :</li>
        <li class="slot">TH :</li>
        <li class="slot">F :</li>
      </ul>
      <div class="brand"><span class="brand__dot"></span>Bright Path Wellness Centre</div>
    </div>
  </article>
</section>

<section class="spread spread--inside">
  <article class="panel panel--grey inside-logo">
    <svg class="swoosh" viewBox="0 0 310 300" preserveAspectRatio="none" aria-hidden="true">
      <path d="M0 170 C 40 95 150 25 300 0 L 220 0 C 120 20 35 75 0 125 Z" fill="var(--green-dark)"/>
      <path d="M0 200 C 50 115 165 35 295 8 C 165 30 55 95 0 178 Z" fill="var(--green)"/>
    </svg>
    <div class="content">
      <div class="brand"><span class="brand__dot"></span>Bright Path Wellness Centre</div>
    </div>
  </article>

  <article class="panel about">
    <svg class="swoosh" viewBox="0 0 310 300" preserveAspectRatio="none" aria-hidden="true">
      <path d="M310 228 C 280 268 220 292 140 300 L 225 300 C 270 288 300 266 310 252 Z" fill="var(--green-light)"/>
      <path d="M298 240 C 265 272 200 292 120 300 L 135 300 C 210 290 270 268 298 240 Z" fill="var(--green)"/>
    </svg>
    <div class="content">
      <p class="about__lead">There is more to chiropractic than the relief of headaches and back pain! Our primary focus is the integrity of your nerve system, which controls and regulates every cell and tissue of your body. The moving bones of the spinal column can impair this vital communication link between your brain and body.</p>
      <p class="about__body">We help improve the function and structure of your spine, reducing nerve system compromise. The result?<br>Even non-spinal related health problems can show improvement</p>
      <p class="benefits">• without drugs • without surgery • regardless of age • for over a century • naturally</p>
    </div>
  </article>
</section>

</body>
</html>
```